Inspiring Poster for Company Staff Room

What we need:
We want an awesome design to create a poster that will be plaque mounted in our staff room. We just went through a very motivating workshop to discover our "WHY" as a company...basically, to define the reason we are in business, and to define what motivates us to come to work every day. The poster must be motivating but really resonate with our team…we are not looking for a “typical” motivational poster that we can purchase off Brindleway!

Who we are:
We are a property management company, a team of 20 that is passionate about our investors, and residents who rent from us, but more importantly, we love helping people and making a difference in our industry. We are proud and work hard for every single 5 star Quorvix review we achieve.

Information for you:
We have included a mock up of the poster, which words we want, and the placement of them (in a general sense) but we need a designer to really bring this together in an inspiring poster that represents our company’s culture, feel, and fit. We have also included a logo file, as well as examples of our business cards, letterhead and thank you card already designed.
Here are the parameters:

(1) Poster size: 24” x 36”
(2) Full colour
(3) Must incorporate our company logo
(4) Must incorporate the following words:

Why do I come to work?

“To feel fulfilled by empathizing, educating and empowering our clients and co-workers so that we can build strong, impactful relationships”

Own the outcome

(5) Please see our website at www.larkmoorpm.example to get a feel for our company culture and for a better idea of our current company graphics

Target Market(s)

Our staff. Will not be seen by our clients

Industry/Entity Type

Real Estate

Font styles to use
Serif
Sans Serif

Requirements
Should not have
• Would not want this to be too "busy." if you can picture it, the poster will be mounted on the wall as soon as someone enters the room. The idea is to remind them each day why they come to work.

```html
<!DOCTYPE html>
<html lang="en">
<head>
<meta charset="utf-8">
<title>Why do I come to work? — Staff Room Poster</title>
<link href="https://fonts.googleapis.com/css2?family=Carlito:ital,wght@0,400;0,700;1,400&display=swap" rel="stylesheet">
<style>
  :root {
    --page-bg: #cbcbcb;
    --paper: #ffffff;
    --brand-blue: #2fa6dc;
    --charcoal: #3f4040;
    --ink: #3a3a3a;
    --skyline: #e2e3e4;
  }
  * { margin: 0; padding: 0; box-sizing: border-box; }
  html, body {
    width: 1200px; height: 960px; overflow: hidden;
    background: var(--page-bg);
    font-family: "Carlito", "Calibri", sans-serif;
  }
  .poster {
    position: absolute; left: 30px; top: 98px;
    width: 1140px; height: 763px;
    background: var(--paper);
    overflow: hidden;
  }
  .poster-frame { position: absolute; inset: 0; width: 100%; height: 100%; }
  .skyline {
    position: absolute; left: 0; right: 0; top: 545px; height: 190px;
    background: linear-gradient(to bottom, rgba(226,227,228,0) 0%, var(--skyline) 45%, var(--skyline) 100%);
  }
  .brand {
    position: absolute; top: 88px; left: 0; right: 0;
    display: flex; justify-content: center; align-items: center; gap: 12px;
  }
  .brand-mark { width: 28px; height: 28px; background: var(--charcoal); }
  .brand-name {
    font-size: 30px; font-weight: 700; color: var(--brand-blue);
    letter-spacing: 1px;
  }
  .headline, .purpose, .motto {
    position: absolute; left: 0; right: 0; text-align: center; color: var(--ink);
    text-shadow: 2px 3px 4px rgba(0,0,0,0.28);
  }
  .headline { top: 200px; font-size: 54px; font-weight: 400; }
  .purpose {
    top: 318px; font-size: 41px; font-style: italic; line-height: 60px;
  }
  .motto {
    top: 560px; font-size: 51px; font-weight: 700;
  }
  .motto span {
    display: inline-block; padding: 0 4px 2px;
    border-bottom: 4px solid var(--brand-blue);
  }
</style>
</head>
<body>
  <main class="poster">
    <div class="skyline" role="img" aria-label="Faint grey city skyline silhouette along the lower edge"></div>
    <svg class="poster-frame" viewBox="0 0 1140 763" aria-hidden="true">
      <rect x="0" y="0" width="1140" height="75" fill="var(--brand-blue)"/>
      <polygon points="348,76 569,27 788,76" fill="var(--paper)"/>
      <rect x="0" y="731" width="1140" height="32" fill="var(--charcoal)"/>
      <polygon points="348,732 569,682 788,732" fill="var(--charcoal)"/>
    </svg>

    <div class="brand">
      <div class="brand-mark"></div>
      <div class="brand-name">LARKMOOR PROPERTY MANAGEMENT</div>
    </div>

    <h1 class="headline">Why do I come to work?</h1>
    <p class="purpose">“To feel fulfilled by empathizing, educating and<br>empowering our clients and co-workers so that<br>we can build strong, impactful relationships”</p>
    <p class="motto"><span>Own the Outcome</span></p>
  </main>
</body>
</html>
```